tiling company needs letterhead urgent

We need a logo to represent our company on an electronic letterhead. We are a tiling firm called Corliss Flooring Ltd and undertake all aspects of tiling work. The final design of the logo should incorporate the type of work we do and should be modern. We do not want any designs which may be considered 'novelty' or 'cartoonish.' No characters please, we require something sleek and contemporary . Please ensure the company name is central to your design ,Corliss Flooring Ltd

Industry/Entity Type

Electronic

Requirements
Must have
• text on letterhead to included

Registered address 58 Brindle grove Hapton Manchester M629QT
Company number 5273908
VAT no 741596238
Mobile no 07812649375
Office no 0161 548 7013
Web :www.surfacecraftexample.co.uk
Email : gerald@surfacecraftexample.co.uk
Nice to have
• a tile theme

```html
<!DOCTYPE html>
<html lang="en">
<head>
<meta charset="utf-8">
<title>Corliss Flooring Ltd — Letterhead</title>
<link href="https://fonts.googleapis.com/css2?family=Questrial&display=swap" rel="stylesheet">
<style>
  :root {
    --backdrop: #a9abb5;
    --paper: #f4f5f8;
    --brown: #4a3b1f;
    --olive: #8c8434;
    --ink: #55575e;
    --rule: #8c8434;
  }
  * { margin: 0; padding: 0; box-sizing: border-box; }
  html, body {
    width: 1200px;
    height: 1000px;
    overflow: hidden;
    background: var(--backdrop);
    font-family: "Questrial", "Century Gothic", sans-serif;
  }
  .letterhead {
    position: absolute;
    left: 270px;
    top: 33px;
    width: 660px;
    height: 934px;
    background: var(--paper);
    box-shadow: 0 6px 24px rgba(40, 42, 50, 0.25);
  }
  .brand {
    position: absolute;
    left: 70px;
    top: 78px;
  }
  .brand-row {
    display: flex;
    align-items: center;
    gap: 12px;
  }
  .brand-mark {
    width: 22px;
    height: 22px;
    background: var(--olive);
  }
  .brand-name {
    font-size: 30px;
    letter-spacing: 1px;
    color: var(--brown);
    text-transform: uppercase;
  }
  .brand-web {
    margin-top: 6px;
    margin-left: 34px;
    font-size: 13px;
    color: var(--olive);
  }
  .footer {
    position: absolute;
    left: 60px;
    right: 60px;
    bottom: 60px;
    display: flex;
    justify-content: space-between;
    font-size: 10.5px;
    line-height: 1.55;
    color: var(--ink);
  }
  .footer-block {
    width: 175px;
    border-top: 1px solid var(--rule);
    padding-top: 8px;
  }
  .label { color: var(--olive); }
</style>
</head>
<body>
  <main class="letterhead">
    <header class="brand">
      <div class="brand-row">
        <span class="brand-mark"></span>
        <span class="brand-name">Corliss Flooring</span>
      </div>
      <div class="brand-web">www.surfacecraftexample.co.uk</div>
    </header>

    <footer class="footer">
      <div class="footer-block contact">
        <div><span class="label">Mobile:</span> 07812649375</div>
        <div><span class="label">Office:</span> 0161 548 7013</div>
        <div><span class="label">Email:</span> gerald@surfacecraftexample.co.uk</div>
      </div>
      <div class="footer-block address">
        <div>58 Brindle grove Hapton</div>
        <div>Manchester M629QT</div>
      </div>
      <div class="footer-block registration">
        <div>Company number: 5273908</div>
        <div>VAT: 741596238</div>
      </div>
    </footer>
  </main>
</body>
</html>
```